Design a new product for a successful cannabis company

We need a package design for a new brand. We are a large cannabis company near Seattle, USA. The name of the product is called the "Velmora Quill". It is a pure cannabis oil extract that is used through a magnetic vaporizer cartridge. We need a graphic template designed that will be printed on a card and inserted into the plastic packaging. This project is design the overall concept, and we will add the required warnings on our end once a design is chosen.

Dimensions:
Width - 2.5625 inches
Height - 3.3125 inches
Viewing Window Width - .4375 inches
Viewing Window Height - 2.0 Inches
Distance from the bottom of the card to the viewing window- .4375 inches
Distance from the left side to the viewing window - 1.0625 inch
Distance from the right side to the viewing window - 1.0625 inch

Theme:
- We would like it to have some sort of Velmora Quill historical feel. I attached the dimensions for size reference. Please extract that "VelmoraQuill" text/font if possible. We really want to use that.
- You could use an old map from that region and time in history.
- Wiki link explaining the Velmora Quill (https://en.lorevault.example/wiki/Velmora_Quill)

Additional Notes:
- There is an area where the physical cartridge will go. Feel free to extend the background into that area but please do not place any text there.
- There is a backside of this package that customers will see. We will place our warning text back there along with a product description. Please keep the back side clear of text but have it match whatever color scheme or background you do on the front side.
- I included an example of a competitor using the same package shape. That's what it will be printed on

Please reach out if you have questions or need clarification. I will be adding details as we go to help with the concept. Thank you!

Target Market(s)

Cannabis oil users of all ages

Colors

Designer to choose colors to be used in the design.

Requirements
Must have
• The same VelmoraQuill text from the attached concert poster
• Must say "A magnetic vape cartridge."
Nice to have
• A historical feel by faintly using an 12th century English map as the background. Open to anything in order to achieve a classic feel.
Should not have
• Bright colors

```html
<!DOCTYPE html>
<html lang="en">
<head>
<meta charset="utf-8">
<title>Velmora Quill – Magnetic Vape Cartridge Card</title>
<link href="https://fonts.googleapis.com/css2?family=Josefin+Sans:wght@300;400;700&family=Cinzel:wght@400;600&display=swap" rel="stylesheet">
<style>
  :root{
    --bg:#ffffff;
    --red:#d8363c;
    --brown:#4a2418;
    --paper-light:#f8e8e2;
    --paper-mid:#efd3c8;
    --paper-deep:#e4bcae;
    --ink:#0d0b0b;
    --plum:#6e2a44;
    --ornament:#b97a94;
    --window:#ece7e2;
    --brass:#c9a24a;
  }
  *{box-sizing:border-box;margin:0;padding:0}
  html,body{width:1200px;height:802px;overflow:hidden;background:var(--bg)}
  .stage{position:relative;width:1200px;height:802px}

  .card{
    position:absolute;width:456px;height:585px;
    background:var(--red);border-radius:40px;padding:8px;
    font-family:"Josefin Sans",sans-serif;color:var(--ink);
  }
  .card--front{left:120px;top:172px;transform:scale(0.908);transform-origin:0 0}
  .card--back{left:636px;top:110px}

  .card__band{position:absolute;inset:8px;background:var(--brown);border-radius:33px}
  .card__paper{
    position:absolute;left:34px;top:36px;width:388px;height:518px;border-radius:22px;overflow:hidden;
    background:
      linear-gradient(100deg,rgba(255,255,255,.35) 0%,rgba(255,255,255,0) 18%,rgba(255,255,255,.3) 38%,rgba(255,255,255,0) 58%,rgba(255,255,255,.35) 80%,rgba(255,255,255,0) 100%),
      linear-gradient(180deg,var(--paper-light),var(--paper-mid) 55%,var(--paper-deep));
  }

  /* all positions below are relative to the card */
  .ornament{position:absolute;background:var(--ornament);opacity:.22;border-radius:14px}
  .ornament--top{left:44px;width:368px;top:46px;height:60px}
  .ornament--frame{left:164px;width:204px;top:222px;height:140px;border-radius:50%;opacity:.2}
  .ornament--rule{left:188px;width:156px;top:380px;height:26px;opacity:.18}
  .ornament--flourish{left:214px;width:100px;top:480px;height:20px;opacity:.2}
  .ornament--bottom{left:44px;width:368px;top:504px;height:40px}

  .brand{
    position:absolute;left:100px;width:324px;top:80px;
    font-weight:700;font-size:50px;line-height:60px;letter-spacing:-1px;
    text-transform:uppercase;text-align:center;
  }
  .tagline{
    position:absolute;left:100px;width:324px;top:244px;
    font-weight:300;font-size:20px;line-height:27px;text-transform:uppercase;text-align:center;
  }
  .tagline span{display:block}
  .tagline .tagline__last{display:inline-block;border-bottom:1.5px dotted var(--ink);line-height:24px}
  .subline{
    position:absolute;left:100px;width:324px;top:384px;
    font-family:"Cinzel",serif;font-size:11px;line-height:14px;letter-spacing:.6px;text-align:center;
  }
  .warning{
    position:absolute;left:144px;width:256px;top:420px;
    font-size:6.4px;line-height:8.6px;text-transform:uppercase;text-align:justify;letter-spacing:-0.1px;
  }
  .warning strong{font-weight:700}

  .window{
    position:absolute;left:48px;top:75px;width:84px;height:440px;border-radius:12px;
    background:linear-gradient(180deg,var(--window) 0 40%,var(--brass) 40% 46%,var(--window) 46% 76%,var(--brass) 76% 86%,var(--window) 86%);
    opacity:.92;
  }
</style>
</head>
<body>
<main class="stage">

  <section class="card card--front">
    <div class="card__band"></div>
    <div class="card__paper"></div>
    <div class="ornament ornament--top" role="img" aria-label="Scrolling filigree border"></div>
    <div class="ornament ornament--frame" role="img" aria-label="Oval filigree frame"></div>
    <div class="ornament ornament--rule" role="img" aria-label="Small filigree flourish"></div>
    <div class="ornament ornament--flourish" role="img" aria-label="Small filigree flourish"></div>
    <div class="ornament ornament--bottom" role="img" aria-label="Scrolling filigree border"></div>
    <div class="window" role="img" aria-label="Clear window showing the vape cartridge"></div>
    <h1 class="brand">Velmora<br>Quill</h1>
    <p class="tagline"><span>A</span><span>Magnetic Vape</span><span class="tagline__last">Cartridge</span></p>
    <p class="subline">P<small>REMIUM PURE CANNABIS OIL</small></p>
    <p class="warning"><strong>Warning:</strong> This package contains marijuana, a schedule I controlled substance. Keep out of reach of children and animals. Marijuana may only be possessed or consumed by persons 21 years of age or older unless the person is a qualified patient. Marijuana use while pregnant or breastfeeding may be harmful. Consumption of marijuana impairs your ability to drive and operate machinery. Please use extreme caution</p>
  </section>

  <section class="card card--back">
    <div class="card__band"></div>
    <div class="card__paper"></div>
    <div class="ornament ornament--top" role="img" aria-label="Scrolling filigree border"></div>
    <div class="ornament ornament--frame" role="img" aria-label="Oval filigree frame"></div>
    <div class="ornament ornament--rule" role="img" aria-label="Small filigree flourish"></div>
    <div class="ornament ornament--flourish" role="img" aria-label="Small filigree flourish"></div>
    <div class="ornament ornament--bottom" role="img" aria-label="Scrolling filigree border"></div>
    <h2 class="brand">Velmora<br>Quill</h2>
    <p class="tagline"><span>A</span><span>Magnetic Vape</span><span class="tagline__last">Cartridge</span></p>
    <p class="subline">P<small>REMIUM PURE CANNABIS OIL</small></p>
    <p class="warning"><strong>Warning:</strong> This package contains marijuana, a schedule I controlled substance. Keep out of reach of children and animals. Marijuana may only be possessed or consumed by persons 21 years of age or older unless the person is a qualified patient. Marijuana use while pregnant or breastfeeding may be harmful. Consumption of marijuana impairs your ability to drive and operate machinery. Please use extreme caution</p>
  </section>

</main>
</body>
</html>
```